Web design for Money Service Business (uncoded)

We need a very basic website with 5-6 pages. Home page, Services, Transfer(How to use our service), About us, Contact us, FAQ
Our company name is Meridale Exchange. We are a company that deals with currency exchange and international money transfer. We do cash exchange and international money transfers to bank accounts all over the world. We offer highly competitive exchange rates so usually attract customers who transfer money over $10,000. Our niche is with larger sums of money, the design needs to be professional and communicate trust, security and stability.

```html
<!DOCTYPE html>
<html lang="en">
<head>
<meta charset="utf-8">
<title>Meridale Exchange – International Money Transfer</title>
<link rel="stylesheet" href="https://fonts.googleapis.com/css2?family=Arimo:wght@400;700&family=Questrial&display=swap">
<style>
:root{
  --navy:#1b4f80;
  --navy-deep:#123a63;
  --orange:#f09a2a;
  --charcoal:#252525;
  --footer:#222222;
  --footer-bottom:#151515;
  --nav-text:#3a3a3a;
  --white:#ffffff;
  --footer-link:#a8a8a8;
}
*{box-sizing:border-box;margin:0;padding:0}
html,body{width:1200px;height:1082px;overflow:hidden;background:var(--white)}
body{position:relative;font-family:"Arimo",Arial,sans-serif;color:var(--nav-text)}
.top-rule{position:absolute;left:0;top:0;width:1200px;height:5px;background:var(--navy-deep)}

.brand{position:absolute;top:34px;left:0;width:1200px;text-align:center}
.brand-name{display:inline-flex;align-items:center;gap:12px;font-family:"Arimo",sans-serif;font-weight:700;font-size:40px;letter-spacing:-0.5px;color:var(--navy)}
.brand-mark{width:34px;height:34px;border-radius:50%;background:var(--orange)}
.brand-tag{font-family:"Questrial",sans-serif;font-size:15px;letter-spacing:3.6px;color:var(--navy);margin-top:2px}

.main-nav{position:absolute;left:120px;top:127px;width:960px;height:43px;background:linear-gradient(#f2f2f2,#dedede)}
.nav-item{font-family:"Questrial",sans-serif;font-size:17px;color:var(--nav-text);position:absolute;top:0;height:43px;line-height:44px;white-space:nowrap}
.nav-item.is-active{left:0;width:90px;background:var(--orange);color:var(--white);text-align:center}
.region-select{position:absolute;left:667px;top:10px;width:278px;height:26px;background:var(--white);border:1px solid #c9c9c9;font-size:13px;line-height:24px;padding-left:8px;color:#444}
.region-select svg{position:absolute;right:8px;top:8px}

.hero{position:absolute;left:120px;top:170px;width:960px;height:375px;background:linear-gradient(110deg,#c9d6e4 0%,#7f93aa 35%,#3c4d63 60%,#8c97a6 85%,#b9c0c8 100%)}
.hero-caption{position:absolute;left:120px;top:365px;width:442px;height:108px;background:var(--orange);color:var(--white);padding:18px 0 0 18px;white-space:nowrap}
.hero-caption .line-light{font-family:"Questrial",sans-serif;font-size:30px;line-height:34px;letter-spacing:0.5px}
.hero-caption .line-bold{font-family:"Arimo",sans-serif;font-weight:700;font-size:27px;line-height:34px;letter-spacing:0.3px;margin-top:2px}

.panel{position:absolute;top:558px;width:310px;height:244px;color:var(--white)}
.panel h2{font-weight:400;font-size:26px;position:absolute;left:20px;top:20px;white-space:nowrap}
.panel-tools{left:120px;background:var(--navy)}
.panel-tools .lead{position:absolute;left:20px;top:68px;width:270px;font-weight:700;font-size:18px;line-height:22px;color:#e3ecf6}
.panel-tools .body{position:absolute;left:20px;top:128px;width:270px;font-size:14px;line-height:18px}
.panel-rates{left:445px;background:var(--charcoal)}
.panel-rates .chart{position:absolute;left:23px;top:65px}
.panel-rates .body{position:absolute;left:23px;top:153px;width:275px;font-size:14px;line-height:18px;color:#dcdcdc}
.read-more{position:absolute;left:23px;top:202px;font-weight:700;font-size:15px;display:flex;align-items:center;gap:9px}
.read-more .plus{width:14px;height:14px;background:var(--white);position:relative}
.read-more .plus::before,.read-more .plus::after{content:"";position:absolute;background:var(--charcoal)}
.read-more .plus::before{left:3px;top:6px;width:8px;height:2px}
.read-more .plus::after{left:6px;top:3px;width:2px;height:8px}
.panel-exchange{left:770px;background:var(--orange)}
.panel-exchange h2{top:14px}
.field-label{position:absolute;left:22px;font-size:15px}
.field-select{position:absolute;left:22px;width:262px;height:24px;background:var(--white);color:#333;font-size:12px;line-height:24px;padding-left:6px}
.field-select svg{position:absolute;right:8px;top:8px}
.amount-input{position:absolute;left:22px;top:191px;width:108px;height:24px;background:var(--white);color:#888;font-size:12px;line-height:24px;padding-left:6px}
.compare-btn{position:absolute;left:205px;top:187px;width:78px;height:30px;background:var(--white);color:var(--navy);border-radius:3px;font-size:17px;text-align:center;line-height:30px}

.footer-rule{position:absolute;left:0;top:820px;width:1200px;height:5px;background:var(--orange)}
.site-footer{position:absolute;left:0;top:825px;width:1200px;height:208px;background:var(--footer)}
.footer-col{position:absolute;top:29px}
.footer-col h3{font-weight:400;font-size:14px;color:var(--orange);margin-bottom:6px;white-space:nowrap}
.footer-col li{list-style:none;font-size:12.5px;line-height:21.5px;color:var(--footer-link);white-space:nowrap}
.legal-bar{position:absolute;left:0;top:1033px;width:1200px;height:49px;background:var(--footer-bottom);font-size:12px;color:var(--footer-link)}
.legal-links{position:absolute;left:120px;top:18px;display:flex;gap:21px}
.copyright{position:absolute;right:120px;top:18px}
</style>
</head>
<body>
<div class="top-rule"></div>

<header class="brand">
  <div class="brand-name"><span class="brand-mark"></span>MERIDALE EXCHANGE</div>
  <div class="brand-tag">INTERNATIONAL MONEY TRANSFER</div>
</header>

<nav class="main-nav">
  <span class="nav-item is-active">HOME</span>
  <span class="nav-item" style="left:113px">ABOUT US</span>
  <span class="nav-item" style="left:233px">SERVICES</span>
  <span class="nav-item" style="left:350px">TRANSFER</span>
  <span class="nav-item" style="left:470px">CONTACT US</span>
  <div class="region-select">Select your region
    <svg width="16" height="9" viewBox="0 0 16 9"><path d="M0 0h16L8 9z" fill="#222"/></svg>
  </div>
</nav>

<div class="hero" role="img" aria-label="Photo of smiling business professionals in an office, a man holding glasses in the foreground"></div>
<div class="hero-caption">
  <div class="line-light">AENEAN DAPIBUS LOREM</div>
  <div class="line-bold">LAOREET ANTE PHARETRA</div>
</div>

<section class="panel panel-tools">
  <h2>Currency Tools</h2>
  <p class="lead">Lorem ipsum dolor sit amet, consectetur adipiscing elit.</p>
  <p class="body">Nullam tempus consequat mi a, tristique leo placerat nec. Praesent tristique eros ac arcu aliquet iaculis.</p>
</section>

<section class="panel panel-rates">
  <h2>Live Rates</h2>
  <svg class="chart" width="260" height="80" viewBox="0 0 260 80">
    <defs><linearGradient id="chartBg" x1="0" y1="0" x2="0" y2="1"><stop offset="0" stop-color="#2c7bd0"/><stop offset="1" stop-color="#0f4c95"/></linearGradient></defs>
    <rect width="260" height="80" fill="url(#chartBg)"/>
    <g stroke="#5f9ee0" stroke-width="0.6" opacity="0.6">
      <line x1="0" y1="16" x2="260" y2="16"/><line x1="0" y1="32" x2="260" y2="32"/><line x1="0" y1="48" x2="260" y2="48"/><line x1="0" y1="64" x2="260" y2="64"/>
      <line x1="52" y1="0" x2="52" y2="80"/><line x1="104" y1="0" x2="104" y2="80"/><line x1="156" y1="0" x2="156" y2="80"/><line x1="208" y1="0" x2="208" y2="80"/>
    </g>
    <polyline fill="none" stroke="#e8f4ff" stroke-width="1.3" points="0,70 10,66 18,68 26,58 34,60 42,48 50,52 58,36 66,40 72,30 80,34 90,28 100,32 108,22 116,36 124,24 132,27 142,20 150,25 160,21 170,26 180,18 190,22 200,16 210,20 220,14 228,17 236,10 240,40 246,20 252,70 260,75"/>
    <rect x="236" y="5" width="9" height="9" fill="#f2d43a"/>
  </svg>
  <p class="body">Lorem ipsum dolor sit amet, consectetur adipiscing elit. Mauris</p>
  <div class="read-more"><span class="plus"></span>Read More</div>
</section>

<section class="panel panel-exchange">
  <h2>Live Exchange Rates</h2>
  <span class="field-label" style="top:63px">Currency from:</span>
  <div class="field-select" style="top:86px">GBP - Great British Pound
    <svg width="14" height="8" viewBox="0 0 14 8"><path d="M0 0h14L7 8z" fill="#222"/></svg>
  </div>
  <span class="field-label" style="top:115px">Currency to:</span>
  <div class="field-select" style="top:137px">EUR - Euro
    <svg width="14" height="8" viewBox="0 0 14 8"><path d="M0 0h14L7 8z" fill="#222"/></svg>
  </div>
  <span class="field-label" style="top:168px">Amount:</span>
  <div class="amount-input">0</div>
  <div class="compare-btn">Compair</div>
</section>

<div class="footer-rule"></div>
<footer class="site-footer">
  <div class="footer-col" style="left:122px"><h3>Personal</h3><ul><li>Online Transfers</li><li>Telephone Transfers</li><li>Regular Transfers</li><li>Other Services</li></ul></div>
  <div class="footer-col" style="left:267px"><h3>Business</h3><ul><li>Online Payments</li><li>FX Dealing</li><li>Corporate FXA</li><li>Other Services</li></ul></div>
  <div class="footer-col" style="left:402px"><h3>Why Meridale Exchange</h3><ul><li>About Us</li><li>Customer Mission</li><li>Behind The Scenes</li><li>Latest News</li><li>Regulatory</li></ul></div>
  <div class="footer-col" style="left:567px"><h3>Marketwatch</h3><ul><li>Live Exchange Rates</li><li>Currency Charts</li><li>Market Briefings</li></ul></div>
  <div class="footer-col" style="left:735px"><h3>Contact us</h3><ul><li>Personal</li><li>Business</li><li>Careers</li></ul></div>
  <div class="footer-col" style="left:852px"><h3>Register</h3><ul><li>Personal</li><li>Business</li></ul></div>
  <div class="footer-col" style="left:943px"><h3>Manage my account</h3><ul><li>Log in</li><li>Forgotten password</li><li>Get a quote</li><li>Make a transfer</li><li>Track a payment</li><li>Change of address</li><li>Help</li></ul></div>
</footer>
<div class="legal-bar">
  <div class="legal-links"><span>Privacy Policy</span><span>Disclaimer</span><span>Complaints Charter</span><span>Staying Safe</span><span>Affiliates</span><span>Registration</span><span>Sitemap</span></div>
  <div class="copyright">© Copyright Meridale Exchange 2013.</div>
</div>
</body>
</html>
```